Website/Logo Design

We need a logo and website design for an opinion mining startup called VantroLux. Our technology mines the web to automatically discover what people are saying about brands, products, etc. The project we are fielding here is for our informational, public-facing website. In its initial incarnation, it will simply be a vehicle for marketing materials and information on our company and its offerings, but it should be flexible enough to expand as more content/functionality is added.

Some designs we like are:
http://www.brivel-nodo.com
http://www.tarnwisp.com
http://www.kvh.com
http://www.zellmorit.com
http://quontavel.com
http://marbiquex.com
http://www.vadup.com
Updates

All, please try to shy away from using a photo of a person as the focal point of the design.  Our company is more technological than social.

Target Market(s)

Primarily businesses interested in sentiment analysis (typically companies involved in advertising, market research, PR, etc.)

Industry/Entity Type

It Company

Requirements
Must have
• We are looking for a clean, modern, and professional design. This includes a logo, homepage, and internal page if it will differ from the homepage.
Nice to have
• It would be excellent if you could provide an HTML mockup if your design is chosen.
Should not have
• Flash, excessive bells and whistles

```html
<!DOCTYPE html>
<html lang="en">
<head>
<meta charset="utf-8">
<title>VantroLux</title>
<link href="https://fonts.googleapis.com/css2?family=PT+Sans:wght@400;700&family=Tinos&display=swap" rel="stylesheet">
<style>
:root{
  --teal:#137089;
  --teal-dark:#0d5367;
  --ink:#1f1f1f;
  --header-top:#dff0fb;
  --header-bottom:#c4e4f7;
  --nav-top:#14687f;
  --nav-bottom:#0b4f62;
  --content-bg:#e9e7e8;
  --footer-bg:#231f20;
  --client-grey:#8a8a8a;
  --body-text:#1a1a1a;
}
*{box-sizing:border-box;margin:0;padding:0}
html,body{width:1200px;height:1123px;overflow:hidden}
body{position:relative;font-family:"PT Sans",Tahoma,sans-serif;color:var(--ink);background:var(--content-bg)}
.site-header{position:absolute;left:0;top:0;width:1200px;height:186px;background:linear-gradient(#eef8fd,var(--header-bottom))}
.brand{position:absolute;left:58px;top:48px;font-size:64px;font-weight:700;color:var(--ink);letter-spacing:-1px}
.call-us{position:absolute;right:55px;top:8px;text-align:right}
.call-us .label{font-size:24px;font-weight:700;color:var(--teal);letter-spacing:1px;line-height:28px}
.call-us .tel{font-size:22px;color:#111;line-height:26px}
.login{position:absolute;left:820px;top:76px;width:330px;font-family:Tahoma,"PT Sans",sans-serif}
.login .title{font-size:16px;margin-bottom:6px}
.login .field{position:absolute;top:28px;width:156px;height:24px;border:1px solid #aab;background:#fff;font-size:12px;color:#888;padding:4px 6px}
.login .user{left:0}.login .pass{left:170px}
.login .button{position:absolute;left:0;top:69px;width:53px;height:24px;background:#8fc2d8;border:1px solid #4c7f95;font-size:12px;text-align:center;line-height:22px}
.login .links{position:absolute;left:62px;top:73px;font-size:13px;font-weight:700;white-space:nowrap}
.login .links a{color:#000}
.login .new{color:#e00}
.main-nav{position:absolute;left:0;top:186px;width:1200px;height:54px;background:linear-gradient(var(--nav-top),var(--nav-bottom));border-top:2px solid #fff;display:flex;justify-content:center;align-items:center;gap:0}
.main-nav a{color:#fff;text-decoration:none;font-size:20px;padding:0 38px;border-right:2px solid #fff;line-height:20px}
.main-nav a:last-child{border-right:none}
.hero{position:absolute;left:0;top:240px;width:1200px;height:270px;background:linear-gradient(#e4e4e4,#fff 30%,#fff)}
.hero p{position:absolute;left:60px;top:58px;width:712px;text-align:center;font-size:31px;line-height:43px;color:var(--teal-dark)}
.hero .chart{position:absolute;left:744px;top:0;width:456px;height:270px;background:radial-gradient(ellipse at 60% 55%,#c6ccd4 0%,#e6e9ed 45%,#fff 75%)}
.panel{position:absolute;width:536px}
.panel h2{font-weight:700;font-size:18px;color:var(--ink);height:38px;border-bottom:2px dotted #777;padding-top:4px}
.panel h2 span{font-size:26px;color:var(--teal);margin-left:6px}
.panel p{font-family:Verdana,"PT Sans",sans-serif;font-size:12px;line-height:21.6px;margin-top:12px;color:var(--body-text)}
.read-more{position:absolute;left:0;font-size:14px;font-weight:700;color:#000;text-decoration:none;display:flex;align-items:center;gap:5px}
.read-more i{display:inline-block;width:10px;height:10px;background:var(--teal)}
.welcome{left:56px;top:538px}.services{left:637px;top:538px;width:509px}
.who{left:56px;top:747px}.clients{left:637px;top:747px;width:509px}
.client-grid{position:absolute;left:637px;top:810px;width:509px;height:98px;background:#fff;display:grid;grid-template-columns:repeat(4,1fr);align-items:center;justify-items:center;padding:6px 4px}
.client-grid span{font-size:20px;font-weight:700;color:var(--client-grey)}
.site-footer{position:absolute;left:0;top:986px;width:1200px;height:137px;background:var(--footer-bg);color:#fff}
.footer-brand{position:absolute;left:59px;top:16px;font-family:Tinos,serif;font-size:28px;color:var(--teal)}
.address{position:absolute;left:64px;top:54px;font-size:14px;line-height:16.5px}
.divider{position:absolute;left:226px;top:46px;height:68px;border-left:2px dotted #777}
.contact{position:absolute;left:254px;top:52px;font-size:14px;font-weight:700;line-height:16.5px}
.contact b{color:var(--teal)}
.footer-nav{position:absolute;right:54px;top:52px;font-size:13px;text-align:right}
.footer-nav a{color:#fff;text-decoration:none;padding:0 6px;border-right:1px solid #fff}
.footer-nav a:last-child{border-right:none;padding-right:0}
.copyright{position:absolute;right:54px;top:75px;font-size:13px}
</style>
</head>
<body>
<header class="site-header">
  <div class="brand">VantroLux</div>
  <div class="call-us"><div class="label">CALL US</div><div class="tel">Tel : +33(0)6 410. 527.36</div></div>
  <form class="login">
    <div class="title">Log&nbsp; In</div>
    <div class="field user">user name</div>
    <div class="field pass">password</div>
    <div class="button">Log In</div>
    <div class="links"><a href="#">forgot your password</a> ? <span class="new">New ?</span> Sign Up</div>
  </form>
</header>
<nav class="main-nav">
  <a href="#">Home</a><a href="#">About VantroLux</a><a href="#">How We Work</a><a href="#">Case Studies</a><a href="#">Pricing</a><a href="#">Contact</a>
</nav>
<section class="hero">
  <p>Our technology mines the web to automatically discover what people are saying about brands, products, etc.</p>
  <div class="chart" role="img" aria-label="3D silver bar chart with a rising trend arrow"></div>
</section>
<section class="panel welcome">
  <h2>Welcome to<span>VantroLux</span></h2>
  <p>Lorem ipsum dolor sit amet, consectetur adipiscing elit. Maecenas luctus arcu sit amet quam viverra condimentum. Suspendisse aliquam ullamcorper sapien suscipit laoreet. Suspendisse varius sodales lectus sit amet convallis. Vestibulum facilisis condimentum lorem, quis commodo tortor luctus eget.</p>
  <a class="read-more" href="#" style="top:160px"><i></i>read more</a>
</section>
<section class="panel services">
  <h2>our<span>Services</span></h2>
  <p>Lorem ipsum dolor sit amet, consectetur adipiscing elit. Maecenas luctus arcu sit amet quam viverra condimentum. Suspendisse aliquam ullamcorper sapien suscipit laoreet. Suspendisse varius sodales lectus sit amet convallis. Vestibulum facilisis condimentum lorem, quis commodo tortor luctus eget.</p>
  <a class="read-more" href="#" style="top:159px"><i></i>read more</a>
</section>
<section class="panel who">
  <h2>Who<span>We Are</span></h2>
  <p>Lorem ipsum dolor sit amet, consectetur adipiscing elit. Maecenas luctus arcu sit amet quam viverra condimentum. Suspendisse aliquam ullamcorper sapien suscipit laoreet. Suspendisse varius sodales lectus sit amet convallis. Vestibulum facilisis condimentum lorem, quis commodo tortor luctus eget.</p>
  <a class="read-more" href="#" style="top:162px"><i></i>read more</a>
</section>
<section class="panel clients">
  <h2>our<span>Clients</span></h2>
</section>
<div class="client-grid">
  <span>Quellion</span><span>Travimo</span><span>KDR</span><span>Bramfold</span>
  <span>Nortavex</span><span>Aldern Vale</span><span>lumo</span><span>Castwell-Hendry</span>
</div>
<footer class="site-footer">
  <div class="footer-brand">VantroLux</div>
  <div class="address">17 dummy address<br>Dummy Address<br>Dummy Addrses</div>
  <div class="divider"></div>
  <div class="contact"><b>Tel :</b> +33(0)6 41 05 27 36<br><b>Email :</b> hello.team@vantrolux.com<br><b>Skype :</b> lena.marrow</div>
  <nav class="footer-nav"><a href="#">Home</a><a href="#">About VantroLux</a><a href="#">How We Work</a><a href="#">Case Studies</a><a href="#">Pricing</a><a href="#">Clients</a><a href="#">Blogs</a><a href="#">Contact Us</a></nav>
  <div class="copyright">© 2010 vantrolux.com | All rights reserved</div>
</footer>
</body>
</html>
```